Business card for our large format printing and installation business

We want a professional looking business card for our business. We manufacture and install Signs.

On the back of the card add this info
Large Format Graphics Printing & Installations, Event Graphics, Banners, Posters, Vehicle Fleet Graphics, Boat Wraps, Wall Murals, Decals,Displays,Signs,Plaques,Digital Signs

On the Front of the card add the Tallowfern Signs logo, plus On the back of the card add the Orange Tallowfern Wraps logo. The 2 vector logos are attached to the design brief.

Target Market(s)

Local business owners

Contact Information for Business Card

Colors
f37122
f68d4e
f9ba93

Requirements
Must have
• On the Front of the card add the Tallowfern Signs logo, plus On the back of the card add the Orange Tallowfern Wraps logo. The 2 vector logos are attached to the design brief.

```html
<!DOCTYPE html>
<html lang="en">
<head>
<meta charset="UTF-8">
<title>Tallowfern Business Card</title>
<link href="https://fonts.googleapis.com/css2?family=Open+Sans:wght@400;600;700&display=swap" rel="stylesheet">
<style>
  :root {
    --backdrop: #3a3a3c;
    --card: #2b2b2d;
    --accent-yellow: #f7e11c;
    --accent-orange: #f79a2e;
    --brand: #f7b51f;
    --text: #e8e8e8;
    --divider: #8c8c8c;
  }
  * { margin: 0; padding: 0; box-sizing: border-box; }
  html, body { width: 1200px; height: 901px; overflow: hidden; }
  body {
    background: var(--backdrop);
    font-family: "Open Sans", sans-serif;
    display: flex;
    flex-direction: column;
    align-items: center;
    justify-content: center;
    gap: 36px;
  }
  .card {
    position: relative;
    width: 720px;
    height: 400px;
    background: var(--card);
    display: flex;
    align-items: center;
    box-shadow: 0 10px 24px rgba(0,0,0,0.35);
  }
  .card::after {
    content: "";
    position: absolute;
    left: 0; right: 0; bottom: 0;
    height: 12px;
    background: linear-gradient(90deg, var(--accent-yellow), var(--accent-orange));
  }
  .brand-block {
    width: 340px;
    padding-left: 60px;
    display: flex;
    align-items: center;
    gap: 12px;
  }
  .brand-mark {
    width: 18px; height: 18px;
    border-radius: 50%;
    background: var(--brand);
    flex: none;
  }
  .brand-name {
    color: var(--brand);
    font-weight: 700;
    font-size: 30px;
    line-height: 1.1;
  }
  .divider {
    width: 1px;
    height: 130px;
    background: var(--divider);
    margin-right: 28px;
  }
  .services {
    list-style: none;
    color: var(--text);
    font-size: 15px;
    line-height: 1.45;
  }
  .services li span::before {
    content: "";
    display: inline-block;
    width: 7px; height: 7px;
    border-radius: 50%;
    background: var(--brand);
    margin: 0 6px 2px 0;
    vertical-align: middle;
  }
  .services li span + span { margin-left: 8px; }
  .contact { color: var(--text); }
  .contact-name { color: var(--brand); font-weight: 700; font-size: 27px; line-height: 1.1; }
  .contact-role { font-size: 22px; margin-bottom: 14px; }
  .contact-address { font-size: 21px; line-height: 1.25; margin-bottom: 12px; }
  .contact-line { display: flex; align-items: center; gap: 12px; font-size: 21px; line-height: 1.35; }
  .contact-line svg { width: 20px; height: 20px; flex: none; }
</style>
</head>
<body>
  <section class="card card-back">
    <div class="brand-block">
      <span class="brand-mark"></span>
      <span class="brand-name">Tallowfern Signs</span>
    </div>
    <div class="divider"></div>
    <ul class="services">
      <li><span>Graphics Printing &amp; Installations</span></li>
      <li><span>Event Graphics</span><span>Banners</span></li>
      <li><span>Posters</span><span>Vehicle Fleet Graphics</span></li>
      <li><span>Boat Wraps</span><span>Wall Murals</span></li>
      <li><span>Decals</span><span>Displays,Signs</span></li>
      <li><span>Plaques</span><span>Digital Signs</span></li>
    </ul>
  </section>

  <section class="card card-front">
    <div class="brand-block">
      <span class="brand-mark"></span>
      <span class="brand-name">Tallowfern Wraps</span>
    </div>
    <div class="divider"></div>
    <div class="contact">
      <p class="contact-name">Marcus Ellery</p>
      <p class="contact-role">Manager</p>
      <p class="contact-address">Your address, city<br>state, ZIP 0000</p>
      <p class="contact-line">
        <svg viewBox="0 0 24 24" aria-hidden="true"><path fill="#f7b51f" d="M6.6 10.8a15.1 15.1 0 0 0 6.6 6.6l2.2-2.2a1 1 0 0 1 1-.25 11.4 11.4 0 0 0 3.6.57 1 1 0 0 1 1 1V20a1 1 0 0 1-1 1A17 17 0 0 1 3 4a1 1 0 0 1 1-1h3.5a1 1 0 0 1 1 1c0 1.25.2 2.45.57 3.57a1 1 0 0 1-.25 1z"/></svg>
        123-456-2100
      </p>
      <p class="contact-line">
        <svg viewBox="0 0 24 24" aria-hidden="true"><rect x="2" y="5" width="20" height="14" fill="#f7b51f"/><path d="M2 5l10 8 10-8" fill="none" stroke="#2b2b2d" stroke-width="2"/></svg>
        youremail@mailbox.com
      </p>
      <p class="contact-line">
        <svg viewBox="0 0 24 24" aria-hidden="true"><circle cx="12" cy="12" r="10" fill="#f7b51f"/><circle cx="12" cy="12" r="4" fill="#2b2b2d"/></svg>
        www.yourwebsite.com
      </p>
    </div>
  </section>
</body>
</html>
```